TR Advisory Business Cards - High End AV / Low Voltage Company

We are low voltage AV company that specializes in high end clients on the residential side and larger businesses on the commercial side. We want something modern, tech looking but also something that is extremely professional looking. We have uploaded our logos and postcards we already have in the field. Along with a picture of one of our wrapped vans. Our website is at www.trvadvisory.example and our primary colors are the orange, green, grey and blue all military color finishes.

We are interesting in the slogans "Pairing You with the Right Technology" or "Leading the Lowcountry in Tech"

Target Market(s)

We focus on 70% Commercial and 30% Residential Customers

Industry/Entity Type

Low Voltage, AV Company

Contact Information for Business Card

Name - Dorian Fairweather, Title - Owner, Office Phone - 555-714-3096, Mobile Phone - 555-802-4173, E-Mail - d@trvadvisory.example, Website: www.trvadvisory.example

Font styles to use
Sans Serif

Requirements
Must have
• Must have Name, Title, Work Phone & Mobile, Website and Logo.
Nice to have
• We want something that will impress our higher end clients with a great logo
Should not have
• Too traditional or plain.

```html
<!DOCTYPE html>
<html lang="en">
<head>
<meta charset="utf-8">
<title>TR Advisory Business Cards</title>
<link href="https://fonts.googleapis.com/css2?family=Montserrat:wght@500;600;700&amp;family=Roboto:wght@400;700&amp;display=swap" rel="stylesheet">
<style>
  :root {
    --backdrop: #d9d9d9;
    --charcoal: #2f2f2f;
    --paper: #ffffff;
    --orange: #ec6530;
    --grey-band: #5a5a5a;
    --text-dark: #333333;
    --text-muted: #777777;
    --divider: #c4c4c4;
  }
  * { box-sizing: border-box; margin: 0; padding: 0; }
  html, body { width: 1200px; height: 874px; overflow: hidden; }
  body {
    background: var(--backdrop);
    position: relative;
    font-family: "Roboto", Arial, sans-serif;
  }
  .card {
    position: absolute;
    left: 290px;
    width: 620px;
    height: 354px;
    border-radius: 22px;
    overflow: hidden;
    box-shadow: 0 10px 24px rgba(0,0,0,0.25);
  }
  .card-back { top: 64px; background: var(--charcoal); }
  .card-front { top: 456px; background: var(--paper); }

  .brand {
    display: flex;
    align-items: center;
    gap: 14px;
    font-family: "Montserrat", sans-serif;
    font-weight: 700;
    color: var(--orange);
    white-space: nowrap;
  }
  .brand-dot { border-radius: 50%; border: 5px solid var(--orange); flex: none; }
  .card-back .brand {
    position: absolute; left: 0; right: 0; top: 0; bottom: 0;
    justify-content: center; font-size: 52px; letter-spacing: 1px;
  }
  .card-back .brand-dot { width: 44px; height: 44px; }

  .card-front .brand {
    position: absolute; left: 34px; top: 118px; font-size: 30px; gap: 10px;
  }
  .card-front .brand-dot { width: 26px; height: 26px; border-width: 4px; }

  .divider {
    position: absolute; left: 272px; top: 70px; width: 1px; height: 150px;
    background: var(--divider);
  }
  .person { position: absolute; left: 300px; top: 74px; }
  .person-name {
    font-weight: 700; font-size: 27px; color: var(--orange); letter-spacing: 0.3px;
  }
  .person-title { font-size: 15px; color: var(--text-muted); }
  .contacts { position: absolute; left: 300px; top: 150px; list-style: none; }
  .contacts li {
    display: flex; align-items: center; gap: 10px;
    font-size: 17px; color: var(--text-dark); line-height: 23px;
  }
  .contacts svg { width: 14px; height: 14px; fill: var(--orange); flex: none; }

  .wave { position: absolute; left: 0; top: 0; width: 620px; height: 354px; }
  .website {
    position: absolute; right: 34px; bottom: 12px;
    font-size: 15px; line-height: 18px; color: var(--paper); letter-spacing: 0.2px;
  }
</style>
</head>
<body>
  <section class="card card-back">
    <div class="brand"><span class="brand-dot"></span>TR Advisory</div>
  </section>

  <section class="card card-front">
    <div class="brand"><span class="brand-dot"></span>TR Advisory</div>
    <div class="divider"></div>
    <div class="person">
      <p class="person-name">Dorian Fairweather</p>
      <p class="person-title">Owner</p>
    </div>
    <ul class="contacts">
      <li><svg viewBox="0 0 24 24"><path d="M6.6 10.8a15 15 0 0 0 6.6 6.6l2.2-2.2a1 1 0 0 1 1-.25 11.4 11.4 0 0 0 3.6.57 1 1 0 0 1 1 1V20a1 1 0 0 1-1 1A17 17 0 0 1 3 4a1 1 0 0 1 1-1h3.5a1 1 0 0 1 1 1c0 1.25.2 2.45.57 3.57a1 1 0 0 1-.25 1z"/></svg>555-714-3096</li>
      <li><svg viewBox="0 0 24 24"><path d="M7 1h10a2 2 0 0 1 2 2v18a2 2 0 0 1-2 2H7a2 2 0 0 1-2-2V3a2 2 0 0 1 2-2zm0 3v14h10V4z"/></svg>555-802-4173</li>
      <li><svg viewBox="0 0 24 24"><path d="M2 5h20v14H2zm2 2v.5l8 5 8-5V7z"/></svg>d@trvadvisory.example</li>
    </ul>
    <svg class="wave" viewBox="0 0 620 354" preserveAspectRatio="none" aria-hidden="true">
      <path d="M0 240 C140 280 260 330 380 300 C470 278 550 250 620 240 L620 354 L0 354 Z" fill="var(--grey-band)"/>
      <path d="M0 256 C140 300 260 348 380 316 C470 294 550 266 620 256 L620 354 L0 354 Z" fill="var(--paper)"/>
      <path d="M0 264 C140 310 260 354 380 322 C470 300 550 272 620 262 L620 354 L0 354 Z" fill="var(--orange)"/>
    </svg>
    <p class="website">www.trvadvisory.example</p>
  </section>
</body>
</html>
```